Ridgeline Orchards Organic Cherry POS card 7x11

We are wanting to create a one-sided 7 x 11 organic cherry card that is eye catching and informative.This should be clear and easy to read and not cluttered. We use these cards as a display in grocery stores, demo stands, and other events to market Organic Ridgeline Sweet Orchards. We have a few facts that we would like displayed on the card (see attachment).

Target Market(s)

Consumers

Industry/Entity Type

Agriculture

Requirements
Must have
• Natural color palettes
• Easy to read
• Ridgeline Orchards
Nice to have
• Unique, realistic cherry design

```html
<!DOCTYPE html>
<html lang="en">
<head>
<meta charset="utf-8">
<title>Ridgeline Orchards – Organic Cherry Card</title>
<link href="https://fonts.googleapis.com/css2?family=Barlow+Semi+Condensed:wght@600;700&display=swap" rel="stylesheet">
<style>
  :root {
    --sky: #cfeaed;
    --sky-deep: #bde2e6;
    --crimson: #9a1747;
    --ink: #111111;
    --cherry-dark: #4a0a18;
    --cherry-mid: #7e1426;
    --cherry-light: #a4283a;
    --bowl: #eeeeec;
  }
  * { margin: 0; padding: 0; box-sizing: border-box; }
  html, body { width: 1200px; height: 764px; overflow: hidden; }
  body { font-family: "Barlow Semi Condensed", "Arial Narrow", sans-serif; }

  .card {
    position: relative;
    width: 1200px;
    height: 764px;
    overflow: hidden;
    background: radial-gradient(ellipse at 70% 40%, var(--sky) 0%, var(--sky-deep) 100%);
  }

  .cherry-photo {
    position: absolute;
    left: 0;
    top: 0;
    width: 640px;
    height: 764px;
    background: radial-gradient(ellipse 330px 420px at 34% 60%,
      var(--cherry-light) 0%,
      var(--cherry-mid) 38%,
      var(--cherry-dark) 70%,
      rgba(238, 238, 236, 0.9) 82%,
      rgba(238, 238, 236, 0) 100%);
  }

  .brand {
    position: absolute;
    left: 34px;
    top: 60px;
    display: flex;
    align-items: center;
    gap: 8px;
    color: var(--crimson);
    font-weight: 700;
    font-size: 22px;
    line-height: 1;
    text-transform: uppercase;
  }
  .brand-dot {
    width: 16px; height: 16px;
    border-radius: 50%;
    background: var(--crimson);
  }

  .headline {
    position: absolute;
    left: 660px;
    top: 0;
    width: 508px;
    height: 300px;
    font-weight: 700;
    text-transform: uppercase;
    color: var(--ink);
  }
  .headline span { position: absolute; right: 0; white-space: nowrap; line-height: 1; }
  .headline .line-region { top: 28px; font-size: 55px; letter-spacing: 0.5px; }
  .headline .line-fruit { top: 70px; font-size: 121px; color: var(--crimson); }
  .headline .line-share { top: 171px; font-size: 76px; }
  .headline .line-nation { top: 243px; font-size: 43px; }

  .fact-box {
    position: absolute;
    left: 698px;
    top: 324px;
    width: 468px;
    height: 170px;
  }
  .fact-box svg { position: absolute; inset: 0; }
  .fact-text {
    position: absolute;
    left: 40px;
    top: 24px;
    color: var(--crimson);
    font-weight: 700;
    text-transform: uppercase;
  }
  .fact-text span { display: block; white-space: nowrap; }
  .fact-text .lead { font-size: 44px; line-height: 46px; }
  .fact-text .middle { font-size: 28px; line-height: 30px; }
  .fact-text .close { font-size: 43px; line-height: 46px; }

  .benefits {
    position: absolute;
    left: 761px;
    top: 530px;
    width: 370px;
    text-align center;
    text-align: center;
    color: var(--ink);
    text-transform: uppercase;
  }
  .benefits h2 { font-size: 39px; font-weight: 700; line-height: 44px; margin-bottom: 2px; }
  .benefits ul { list-style: none; }
  .benefits li { font-size: 26px; font-weight: 600; line-height: 32px; }
</style>
</head>
<body>
  <main class="card">
    <div class="cherry-photo" role="img" aria-label="White bowl of fresh organic dark red cherries with stems, covered in water droplets"></div>

    <div class="brand"><span class="brand-dot"></span>Ridgeline Orchards</div>

    <h1 class="headline">
      <span class="line-region">Organic Ridgeline</span>
      <span class="line-fruit">Cherries</span>
      <span class="line-share">Make up 1/3 of</span>
      <span class="line-nation">The nation’s production.</span>
    </h1>

    <section class="fact-box">
      <svg width="468" height="170" viewBox="0 0 468 170" aria-hidden="true">
        <path d="M12 2 H456 V12 H466 V158 H456 V168 H12 V158 H2 V12 H12 Z" fill="none" stroke="var(--crimson)" stroke-width="4"/>
        <rect x="14" y="14" width="440" height="142" fill="none" stroke="var(--crimson)" stroke-width="2"/>
      </svg>
      <p class="fact-text">
        <span class="lead">Washington State is</span>
        <span class="middle">The nation’s largest producer</span>
        <span class="close">of organic cherries.</span>
      </p>
    </section>

    <section class="benefits">
      <h2>Health Benefits</h2>
      <ul>
        <li>Fat free</li>
        <li>Source of vitamin C</li>
        <li>Natural anti-inflammatory</li>
        <li>Source of potassium</li>
        <li>Source of melatonin</li>
      </ul>
    </section>
  </main>
</body>
</html>
```